Business Card Design for Property Investment Company

We need a new business card designed that reflects our new domain. and also reflects more closely the style and branding of our website www.kmvholdings.co.uk

The template will be the same for two different directors. Logo and images from website, as well as more detail on brief are attached

Want a two-side design
Details from above image need to change as follows:
E: owen.baxley@kmvholdings.co.uk
W: www.kmvholdings.co.uk

Also, need second card, same design, for:
Martin Baxley
Director
M: +44 (0)7812 364917
E: martin.baxley@kmvholdings.co.uk
A: same as above
W: same as above

Attached are a selection of images from the website that could be used on the website, as well as the logo

Target Market(s)

Property/Real-estate professionals, invesroea and developers

Industry/Entity Type

Real Estate Development

Contact Information for Business Card

see brief attachment

Font styles to use
Sans Serif

Requirements
Must have
• Contact info as per brief
• Look and feel of the website - www.kmvholdings.co.uk
• (a selection of images that can be used have been attached, along with logo)
• Slick and professional look
Nice to have
• maybe include an image on one side of the card with logo, and contact info on the other (only a suggestion)
Should not have
• anything gimmicky

```html
<!DOCTYPE html>
<html lang="en">
<head>
<meta charset="utf-8">
<title>KMV Holdings – Business Card</title>
<link rel="stylesheet" href="https://fonts.googleapis.com/css2?family=Arimo:wght@400;700&display=swap">
<style>
  :root {
    --stage: #2b2b2b;
    --card: #f7f7f7;
    --ink: #111111;
    --ink-soft: #4a4a4a;
    --rule: #1a1a1a;
    --photo-light: #f2f3f4;
    --photo-mid: #b9bec3;
    --photo-dark: #3a3f44;
  }
  * { box-sizing: border-box; margin: 0; padding: 0; }
  html, body {
    width: 1200px;
    height: 873px;
    overflow: hidden;
    background: var(--stage);
    font-family: "Arimo", Arial, sans-serif;
  }
  .card-set {
    position: absolute;
    top: 286px;
    left: 60px;
    display: flex;
    gap: 40px;
  }
  .card {
    position: relative;
    width: 520px;
    height: 300px;
    border-radius: 22px;
    overflow: hidden;
    background: var(--card);
  }
  /* Front: skyline photograph with centred mark */
  .card-front .skyline-photo {
    position: absolute;
    inset: 0;
    background:
      radial-gradient(ellipse 38% 48% at 50% 50%, var(--photo-light) 0%, rgba(242,243,244,0.85) 45%, rgba(242,243,244,0) 100%),
      linear-gradient(135deg, var(--photo-dark) 0%, var(--photo-mid) 45%, var(--photo-mid) 55%, var(--photo-dark) 100%);
  }
  .brand-mark {
    display: flex;
    align-items: center;
    gap: 8px;
    font-weight: 700;
    color: var(--ink);
  }
  .brand-mark .brand-dot {
    border-radius: 50%;
    background: var(--ink);
  }
  .card-front .brand-mark {
    position: absolute;
    top: 50%;
    left: 50%;
    transform: translate(-50%, -50%);
    font-size: 30px;
  }
  .card-front .brand-dot { width: 22px; height: 22px; }

  /* Back: contact details */
  .card-back .brand-mark {
    position: absolute;
    top: 30px;
    right: 34px;
    font-size: 26px;
  }
  .card-back .brand-dot { width: 18px; height: 18px; }
  .identity {
    position: absolute;
    left: 34px;
    right: 34px;
    top: 140px;
    display: flex;
    align-items: flex-end;
    gap: 8px;
  }
  .identity-name {
    font-size: 21px;
    font-weight: 700;
    color: var(--ink);
    line-height: 1;
    white-space: nowrap;
  }
  .identity-rule {
    flex: 1;
    height: 2px;
    background: var(--rule);
    margin-bottom: 4px;
  }
  .identity-role {
    position: absolute;
    left: 34px;
    top: 166px;
    font-size: 10px;
    font-weight: 700;
    letter-spacing: 0.5px;
    color: var(--ink-soft);
    text-transform: uppercase;
  }
  .contact-list {
    position: absolute;
    left: 34px;
    top: 196px;
    list-style: none;
    font-size: 13px;
    color: var(--ink-soft);
    line-height: 1.2;
  }
  .contact-list li {
    display: flex;
    align-items: flex-start;
    gap: 8px;
    margin-bottom: 6px;
  }
  .contact-icon {
    flex: none;
    width: 16px;
    height: 16px;
  }
  .web-address {
    position: absolute;
    right: 34px;
    top: 226px;
    font-size: 13px;
    font-weight: 700;
    color: var(--ink);
  }
</style>
</head>
<body>
  <main class="card-set">
    <section class="card card-front" aria-label="Card front">
      <div class="skyline-photo" role="img" aria-label="Upward view of glass office towers converging into a misty white sky"></div>
      <div class="brand-mark"><span class="brand-dot"></span><span>kmv</span></div>
    </section>

    <section class="card card-back" aria-label="Card back">
      <div class="brand-mark"><span class="brand-dot"></span><span>kmv</span></div>

      <div class="identity">
        <h1 class="identity-name">Owen Baxley</h1>
        <span class="identity-rule"></span>
      </div>
      <p class="identity-role">Founder &amp; CEO</p>

      <ul class="contact-list">
        <li>
          <svg class="contact-icon" viewBox="0 0 16 16" aria-hidden="true">
            <circle cx="8" cy="8" r="8" fill="#111"/>
            <path d="M5.2 4.2l1.3-.3.8 1.8-.9.7c.4.9 1.1 1.7 2 2.1l.7-.9 1.8.8-.3 1.3c-.2.4-.6.6-1 .5C6.9 9.7 5.1 7.9 4.7 5.2c-.1-.4.1-.8.5-1z" fill="#fff"/>
          </svg>
          <span>+44 (0)7812 364917</span>
        </li>
        <li>
          <svg class="contact-icon" viewBox="0 0 16 16" aria-hidden="true">
            <circle cx="8" cy="8" r="8" fill="#111"/>
            <rect x="4" y="5" width="8" height="6" rx="0.6" fill="#fff"/>
            <path d="M4.3 5.4L8 8.3l3.7-2.9" fill="none" stroke="#111" stroke-width="0.9"/>
          </svg>
          <span>owen.baxley@kmvholdings.co.uk</span>
        </li>
        <li>
          <svg class="contact-icon" viewBox="0 0 16 16" aria-hidden="true">
            <circle cx="8" cy="8" r="8" fill="#111"/>
            <path d="M8 3.6a2.9 2.9 0 0 0-2.9 2.9C5.1 8.7 8 12.4 8 12.4s2.9-3.7 2.9-5.9A2.9 2.9 0 0 0 8 3.6z" fill="#fff"/>
            <circle cx="8" cy="6.5" r="1.1" fill="#111"/>
          </svg>
          <span>18 Harrowden Lane, Elmstead<br>Kent BR4 2QL</span>
        </li>
      </ul>

      <p class="web-address">www.kmvholdings.co.uk</p>
    </section>
  </main>
</body>
</html>
```